Steadfast MD - Sleep Medicine Specialist - Business Cards

We are a new medical practice called Steadfast MD. We are sleep medicine specialists and we will be conducting sleep studies on patients with sleep related ailments. We want the business card to be bold, professional, and clean with the logo as the stand out visual piece. We dont like wild flashy designs. We want our design to be bold and classic while at the same time conveying who we are and what we do. We are reliable, professional, and the best in the business.

Industry/Entity Type

Health Care

Contact Information for Business Card

- Clean
- Bold
- Classic
- not cluttered

Requirements
Must have
• logo, website, phone number
Nice to have
• several options to choose from
Should not have
• flashy imaged - reflective print - images of people sleeping

```html
<!DOCTYPE html>
<html lang="en">
<head>
<meta charset="UTF-8">
<title>Steadfast MD – Business Card</title>
<link href="https://fonts.googleapis.com/css2?family=Montserrat:wght@700;800&family=Roboto:wght@400;500&display=swap" rel="stylesheet">
<style>
  :root {
    --red: #e31b23;
    --black: #0b0b0c;
    --white: #ffffff;
    --ink: #222222;
    --grey: #3a3a3a;
    --backdrop: #d9d9d9;
  }
  * { box-sizing: border-box; margin: 0; padding: 0; }
  html, body { width: 1200px; height: 900px; overflow: hidden; }
  body {
    background: var(--backdrop);
    display: flex;
    flex-direction: column;
    align-items: center;
    justify-content: center;
    gap: 56px;
  }
  .card {
    position: relative;
    width: 640px;
    height: 366px;
    overflow: hidden;
    box-shadow: 0 10px 30px rgba(0,0,0,0.25);
  }

  /* Back side */
  .card-back {
    background: var(--black);
    display: flex;
    align-items: center;
    justify-content: center;
  }
  .brand {
    display: flex;
    align-items: center;
    gap: 16px;
  }
  .brand-mark {
    border: 4px solid var(--red);
    border-radius: 50%;
    flex: none;
  }
  .brand-name {
    font-family: "Montserrat", sans-serif;
    font-weight: 800;
    letter-spacing: -0.5px;
  }
  .card-back .brand-mark { width: 78px; height: 78px; }
  .card-back .brand-name { font-size: 50px; color: var(--white); }

  /* Front side */
  .card-front {
    background: var(--white);
    display: flex;
    align-items: center;
    padding: 0 0 24px 34px;
  }
  .card-front .brand { width: 286px; gap: 10px; }
  .card-front .brand-mark { width: 54px; height: 54px; border-width: 3px; }
  .card-front .brand-name { font-size: 30px; color: var(--black); }
  .divider {
    width: 2px;
    height: 132px;
    background: var(--black);
    margin: 0 20px 0 8px;
  }
  .contact-name {
    font-family: "Montserrat", sans-serif;
    font-weight: 700;
    font-size: 19px;
    color: var(--black);
    letter-spacing: 0.3px;
  }
  .contact-name .surname { color: var(--red); }
  .contact-role {
    font-family: "Roboto", sans-serif;
    font-weight: 500;
    font-size: 17px;
    color: var(--grey);
    margin-bottom: 10px;
  }
  .contact-list { list-style: none; }
  .contact-list li {
    display: flex;
    align-items: center;
    gap: 9px;
    font-family: "Roboto", sans-serif;
    font-size: 17px;
    color: var(--ink);
    line-height: 1.45;
  }
  .contact-list svg { width: 16px; height: 16px; flex: none; }

  .edge-band {
    position: absolute;
    left: 0; right: 0; bottom: 0;
    height: 16px;
  }
  .edge-band .band-dark {
    position: absolute; left: 0; bottom: 0; height: 100%; width: 312px;
    background: var(--black);
  }
  .edge-band .band-red {
    position: absolute; right: 0; bottom: 0; height: 100%; width: 318px;
    background: var(--red);
    clip-path: polygon(16px 0, 100% 0, 100% 100%, 0 100%);
  }
</style>
</head>
<body>

  <section class="card card-back" aria-label="Business card, back">
    <div class="brand">
      <span class="brand-mark"></span>
      <span class="brand-name">Steadfast MD</span>
    </div>
  </section>

  <section class="card card-front" aria-label="Business card, front">
    <div class="brand">
      <span class="brand-mark"></span>
      <span class="brand-name">Steadfast MD</span>
    </div>
    <div class="divider"></div>
    <div class="contact">
      <p class="contact-name">MARTIN <span class="surname">ASHCOMBE</span></p>
      <p class="contact-role">Managing Director</p>
      <ul class="contact-list">
        <li>
          <svg viewBox="0 0 16 16" aria-hidden="true"><path fill="var(--red)" d="M1 5c0-2 3-3 7-3s7 1 7 3v1h-3V4.5C11 4 10 4 8 4S5 4 4 4.5V6H1zM4 7h8l2 7H2z"/></svg>
          020 7946 0182
        </li>
        <li>
          <svg viewBox="0 0 16 16" aria-hidden="true"><rect x="1" y="3" width="14" height="10" fill="var(--red)"/><path d="M1.5 3.5L8 9l6.5-5.5" fill="none" stroke="#fff" stroke-width="1.3"/></svg>
          info@SteadfastMD.com
        </li>
        <li>
          <svg viewBox="0 0 16 16" aria-hidden="true"><circle cx="8" cy="8" r="7" fill="var(--red)"/><ellipse cx="8" cy="8" rx="3" ry="7" fill="none" stroke="#fff" stroke-width="1"/><path d="M1 8h14" stroke="#fff" stroke-width="1"/></svg>
          www.SteadfastMD.com
        </li>
      </ul>
    </div>
    <div class="edge-band">
      <span class="band-dark"></span>
      <span class="band-red"></span>
    </div>
  </section>

</body>
</html>
```